Professional Label needed for Velvet Biscuit Kitchen

I make 100% organic dog treats. Wheat and gluten free.

I will be packaging them in a window kraft bag. I need a nicely designed label to place on each bag. The name of my company is The Velvet Biscuit Kitchen Company. All ingredients are organic and no preservatives are used. They are a healthy alternative to "assembly line" treats made by large companies.

Target Market(s)

Dog Owners

Industry/Entity Type

Pet

Font styles to use
Serif

Colors
00a990

Requirements
Must have
• can use a dog paw - see attached files. Dog themed, 100%
• Organic Dog Treats.
• No preservatives, nothing artificial, no corn, wheat or soy, made in Texas, USA with 100% organic ingredients. Non GMO
• Must have "dog treat" somewhere.
• "The Velvet Biscuit Kitchen Co." font size needs to be bigger than anything else.
Nice to have
• I like teal and brown
• I'm open to anything really as long as its dog themed

```html
<!DOCTYPE html>
<html lang="en">
<head>
<meta charset="utf-8">
<title>The Velvet Biscuit Kitchen Co. – Dog Treat Bag Label</title>
<link rel="stylesheet" href="https://fonts.googleapis.com/css2?family=Dancing+Script:wght@500&family=Tinos:wght@700&display=swap">
<style>
  :root {
    --page: #ffffff;
    --kraft-brown: #75421c;
    --brand-teal: #12a28a;
    --paw-dark: #2b1a12;
    --copy-white: #ffffff;
  }
  html, body {
    margin: 0;
    padding: 0;
    width: 1200px;
    height: 927px;
    overflow: hidden;
    background: var(--page);
  }
  .canvas {
    position: relative;
    width: 1200px;
    height: 927px;
  }
  .label {
    position: absolute;
    left: 327px;
    top: 196px;
    width: 488px;
    height: 501px;
    background: var(--kraft-brown);
    overflow: hidden;
  }
  .paw-mark {
    position: absolute;
    top: 17px;
    width: 56px;
    height: 64px;
  }
  .paw-mark--left { left: 22px; }
  .paw-mark--right { right: 20px; top: 14px; }
  .brand-name {
    position: absolute;
    left: 0;
    right: 0;
    top: 12px;
    margin: 0;
    text-align: center;
    font-family: "Dancing Script", cursive;
    font-weight: 500;
    font-size: 78px;
    line-height: 76px;
    color: var(--brand-teal);
  }
  .brand-name span { display: block; }
  .product-claims {
    position: absolute;
    left: 0;
    right: 0;
    top: 336px;
    margin: 0;
    text-align: center;
    font-family: "Tinos", "Times New Roman", serif;
    font-weight: 700;
    font-size: 22px;
    line-height: 36px;
    color: var(--copy-white);
  }
</style>
</head>
<body>
<main class="canvas">
  <section class="label">
    <svg class="paw-mark paw-mark--left" viewBox="0 0 56 64" role="img" aria-label="Dog paw print">
      <rect x="0" y="0" width="56" height="64" rx="20" fill="var(--paw-dark)"/>
    </svg>
    <svg class="paw-mark paw-mark--right" viewBox="0 0 56 64" role="img" aria-label="Dog paw print">
      <rect x="0" y="0" width="56" height="64" rx="20" fill="var(--paw-dark)"/>
    </svg>

    <h1 class="brand-name">
      <span>The</span>
      <span>Velvet Biscuit</span>
      <span>Kitchen</span>
      <span>Co.</span>
    </h1>

    <p class="product-claims">
      Organic dog treats made in Texas, USA<br>
      with 100% organic ingredients.<br>
      No preservatives, nothing artificial.<br>
      No corn, wheat or soy. Non GMO
    </p>
  </section>
</main>
</body>
</html>
```